I am medical doctor in surgery specialized in Urology and anti-aging. I need Web and Instagram design for a head cream , face cream and body lotion. I did a 2% GHK-Cu solution (head-face-body) with an professional pharmacist specialized in manufacturing creams. . GHK-Cu is a tri-peptide with solid scientific background to rejuvenate the skin (will stimulate collagen production) and can promote hair regrowth. Statistically 70% of peptides bought are fake on the market, I can personally guarantee about purity (my peptides are certified pure above 99% checked in an independent laboratory in London -UK.
I want to use the name 'Lumavex'. I secured already the domain names. I had an design for another project I could re-use for this project. The ribbon should include more blue. The font of Lumavex can be changed. I got a logo which is ok for me. Web design best coded with Wordpress.

Target Market(s)

Anti aging, skin care, hair regrowth, skin collagen

Industry/Entity Type

the cream can also be used after surgery for faster and better wound healing

Number of Pages Required

5+ page

Font styles to use
Sans Serif

Colors
0054AA
0677BA
7BADD7
CADEEF
E8F1F8

Requirements
Must have
• target population 30-70 years
Nice to have
• scientific proof, pictures before-after
Should not have
• GHK-Cu has solid scientific animal studies of anti-cancer properties. It is 100% safe for dermal human use.

```html
<!DOCTYPE html>
<html lang="en">
<head>
<meta charset="utf-8">
<title>Lumavex — About</title>
<link href="https://fonts.googleapis.com/css2?family=Inter:wght@400;500;600;700&display=swap" rel="stylesheet">
<style>
  :root{
    --navy:#0a3a8c;
    --blue:#0054aa;
    --blue-mid:#0677ba;
    --blue-soft:#7badd7;
    --blue-pale:#cadeef;
    --band:#f4f8fc;
    --ink:#0f1626;
    --text:#3c4656;
    --muted:#5b6575;
    --line:#e3e9f1;
    --white:#ffffff;
  }
  *{box-sizing:border-box;margin:0;padding:0}
  html,body{width:1200px;height:884px;overflow:hidden}
  body{font-family:"Inter",Arial,sans-serif;background:var(--white);color:var(--text);position:relative}
  a{color:inherit;text-decoration:none}

  .brand{display:flex;align-items:center;gap:5px;font-weight:600;font-size:12.5px;color:var(--navy);letter-spacing:-0.2px}
  .brand-dot{width:9px;height:9px;border-radius:50%;background:var(--blue)}

  .site-header{height:45px;border-bottom:1px solid var(--line);position:relative}
  .site-header .brand{position:absolute;left:159px;top:14px}
  .main-nav{position:absolute;left:436px;top:15px;display:flex;gap:23px;font-size:10.5px;color:#3a4250}
  .main-nav .current{color:var(--navy);font-weight:500}
  .btn-shop{position:absolute;left:955px;top:10px;width:85px;height:25px;border-radius:13px;background:var(--navy);color:var(--white);font-size:10.5px;font-weight:600;display:flex;align-items:center;justify-content:center}

  .about-intro{position:absolute;left:296px;top:114px;width:610px}
  .eyebrow{font-size:10px;font-weight:500;letter-spacing:1px;color:var(--blue-mid)}
  .about-title{margin-top:11px;font-size:34px;line-height:34px;font-weight:700;letter-spacing:-1.3px;color:var(--ink)}
  .about-copy{margin-top:24px;font-size:11.8px;line-height:16.8px;color:var(--text)}

  .pillars{position:absolute;left:0;top:447px;width:1200px;height:217px;background:var(--band);border-bottom:1px solid var(--line)}
  .pillar-grid{position:absolute;left:159px;top:58px;display:flex;gap:29px}
  .pillar{width:274px;height:101px;background:var(--white);border:1px solid var(--blue-pale);border-radius:8px;padding:24px 23px}
  .pillar h3{font-size:13px;font-weight:600;color:var(--navy);letter-spacing:-0.1px}
  .pillar p{margin-top:10px;font-size:9.6px;line-height:13.5px;color:var(--muted)}

  .site-footer{position:absolute;left:0;top:665px;width:1200px;height:219px;background:var(--band)}
  .footer-about{position:absolute;left:159px;top:40px;width:280px}
  .footer-about p{margin-top:16px;font-size:9.6px;line-height:13.5px;color:var(--muted)}
  .footer-about .note{margin-top:9px;font-size:8px;color:var(--muted)}
  .footer-col{position:absolute;top:46px}
  .footer-col h4{font-size:9.8px;font-weight:600;color:var(--ink)}
  .footer-col ul{list-style:none;margin-top:8px}
  .footer-col li{font-size:9.8px;line-height:19px;color:var(--muted)}
  .col-explore{left:614px}
  .col-legal{left:841px}
  .footer-bar{position:absolute;left:0;top:179px;width:1200px;border-top:1px solid var(--line);height:40px;font-size:8.2px;color:var(--muted)}
  .footer-bar .copy{position:absolute;left:159px;top:15px}
  .footer-bar .disclaimer{position:absolute;right:160px;top:15px}
</style>
</head>
<body>
  <header class="site-header">
    <a class="brand" href="#"><span class="brand-dot"></span>Lumavex</a>
    <nav class="main-nav">
      <a href="#">Home</a>
      <a href="#">The Science</a>
      <a href="#">Products</a>
      <a href="#" class="current">About</a>
      <a href="#">Contact</a>
    </nav>
    <a class="btn-shop" href="#">Shop range</a>
  </header>

  <section class="about-intro">
    <p class="eyebrow">ABOUT</p>
    <h1 class="about-title">A peptide brand founded inside a surgical practice.</h1>
    <div class="about-copy">
      <p>Lumavex was created by a urology and anti-aging surgeon who spent years watching patients invest in peptide skincare that could not be trusted. Independent testing consistently shows that most peptides sold online are underdosed, degraded, or entirely fake.</p>
      <p>Working with a specialist compounding pharmacist, we set out to produce a single active — GHK-Cu at a clinically meaningful 2% concentration — with one non-negotiable standard: purity above 99%, verified by an independent laboratory in London before every batch is released.</p>
      <p>The three-product system — face cream, head cream, body lotion — is designed for adults between 30 and 70 who want measurable improvements in skin quality, hair support, and recovery after surgical or aesthetic procedures.</p>
    </div>
  </section>

  <section class="pillars">
    <div class="pillar-grid">
      <article class="pillar">
        <h3>Physician-formulated</h3>
        <p>Every formulation is co-signed by the founding surgeon.</p>
      </article>
      <article class="pillar">
        <h3>Pharmacist-compounded</h3>
        <p>Manufactured with a specialist compounding pharmacist.</p>
      </article>
      <article class="pillar">
        <h3>Independently verified</h3>
        <p>Purity confirmed above 99% by a London laboratory.</p>
      </article>
    </div>
  </section>

  <footer class="site-footer">
    <div class="footer-about">
      <a class="brand" href="#"><span class="brand-dot"></span>Lumavex</a>
      <p>Certified pure GHK-Cu 2% peptide skincare, formulated by a urologist and anti-aging surgeon with a specialist compounding pharmacist.</p>
      <p class="note">Purity verified &gt;99% by an independent laboratory in London, UK.</p>
    </div>
    <div class="footer-col col-explore">
      <h4>Explore</h4>
      <ul><li>Products</li><li>The Science</li><li>About</li><li>Contact</li></ul>
    </div>
    <div class="footer-col col-legal">
      <h4>Legal</h4>
      <ul><li>Terms of Sale</li><li>Privacy Policy</li><li>Cosmetic Compliance</li></ul>
    </div>
    <div class="footer-bar">
      <span class="copy">© 2026 Lumavex. All rights reserved.</span>
      <span class="disclaimer">For cosmetic use. Not a medicine. Consult your physician for medical advice.</span>
    </div>
  </footer>
</body>
</html>
```